we are a college and require a design of a printable graduation certificate

our courses range from certicate III to Diploma

We would a high quality design, similar to a unveristy degree, so its meaning full to the students and looks great on the wall

our college website is: www.marlowinstitute.example.au

Industry/Entity Type

College

Requirements
Must have
• security feature like water mark or stamp

```html
<!DOCTYPE html>
<html lang="en">
<head>
<meta charset="utf-8">
<title>Marlow Institute – Graduation Certificate</title>
<link rel="stylesheet" href="https://fonts.googleapis.com/css2?family=UnifrakturCook:wght@700&family=UnifrakturMaguntia&display=swap">
<style>
  :root {
    --frame-tan: #d9c99b;
    --frame-light: #ece1bf;
    --frame-line: #b9a56d;
    --frame-dark: #a18d55;
    --paper: #ffffff;
    --ink: #111111;
    --olive: #86814f;
    --olive-dark: #3e3b22;
    --olive-shadow: #9aa39a;
    --ornament: #e6dcc0;
    --watermark: #86814f;
    --signature-area: #f6f6f6;
  }
  * { margin: 0; padding: 0; box-sizing: border-box; }
  html, body { width: 1200px; height: 922px; overflow: hidden; background: #ffffff; }
  .certificate {
    position: relative;
    width: 1200px;
    height: 922px;
    background: var(--frame-tan);
    font-family: "UnifrakturMaguntia", "Old English Text MT", serif;
    color: var(--ink);
    overflow: hidden;
  }
  .frame-outer {
    position: absolute;
    inset: 10px;
    border: 3px solid var(--frame-line);
    background: repeating-linear-gradient(90deg, var(--frame-tan) 0 3px, var(--frame-light) 3px 5px);
  }
  .frame-band {
    position: absolute;
    inset: 30px;
    border: 2px solid var(--frame-dark);
    background: var(--frame-light);
  }
  .frame-inner {
    position: absolute;
    inset: 46px;
    border: 4px double var(--frame-line);
    background: var(--frame-tan);
  }
  .paper {
    position: absolute;
    left: 78px; top: 72px; right: 68px; bottom: 100px;
    background: var(--paper);
    border: 1px solid var(--frame-dark);
    overflow: hidden;
  }
  .watermark {
    position: absolute;
    inset: 0;
    width: 100%;
    height: 100%;
  }
  .watermark text {
    font-family: "UnifrakturMaguntia", serif;
    font-size: 26px;
    fill: var(--watermark);
    fill-opacity: 0.09;
  }
  .corner-ornament {
    position: absolute;
    width: 70px; height: 70px;
    background: radial-gradient(circle, var(--frame-light), var(--ornament) 60%, var(--frame-tan));
    border-radius: 8px;
  }
  .corner-ornament.top-left { left: 0; top: 0; }
  .corner-ornament.top-right { right: 0; top: 0; }
  .corner-ornament.bottom-left { left: 0; bottom: 50px; }
  .corner-ornament.bottom-right { right: 0; bottom: 50px; }

  .institution-title {
    position: absolute;
    left: 70px; top: 62px;
    width: 1030px; height: 220px;
  }
  .institution-title text {
    font-family: "UnifrakturCook", "UnifrakturMaguntia", serif;
    font-weight: 700;
    font-size: 146px;
    fill: var(--olive);
    stroke: var(--olive-dark);
    stroke-width: 2.5px;
    paint-order: stroke;
  }
  .institution-title .title-shadow { fill: var(--olive-shadow); stroke: none; }

  .line {
    position: absolute;
    left: 60px; width: 1050px;
    text-align: center;
    white-space: nowrap;
    line-height: 1;
  }
  .recommendation { top: 228px; font-size: 35px; }
  .faculty { top: 296px; font-size: 53px; }
  .student-name { top: 395px; font-size: 73px; color: var(--olive); text-shadow: 1px 1px 0 var(--olive-dark); }
  .completion { top: 521px; font-size: 34px; }
  .award {
    top: 560px; font-size: 58px; color: var(--olive);
    text-shadow: 1px 1px 0 var(--olive-dark), 3px 3px 2px var(--olive-shadow);
  }
  .rights { top: 620px; font-size: 30px; }
  .presented { top: 655px; font-size: 24px; }

  .signature-block {
    position: absolute;
    text-align: center;
    line-height: 1.1;
    font-size: 16px;
  }
  .signature-block.president { left: 95px; top: 690px; width: 300px; }
  .signature-block.board { left: 715px; top: 690px; width: 370px; }
  .signature-mark {
    height: 80px;
    margin: 0 auto 8px;
    background: var(--signature-area);
  }
  .signature-block.president .signature-mark { width: 280px; }
  .signature-block.board .signature-mark { width: 360px; }

  .seal-panel {
    position: absolute;
    left: 465px; top: 700px;
    width: 245px; height: 222px;
    background: var(--paper);
    display: flex;
    flex-direction: column;
    align-items: center;
    justify-content: flex-end;
    gap: 16px;
    padding-bottom: 26px;
  }
  .seal-square {
    width: 90px; height: 90px;
    border: 3px solid var(--ink);
  }
  .seal-name { font-size: 24px; color: var(--ink); line-height: 1; }
</style>
</head>
<body>
<main class="certificate">
  <div class="frame-outer"></div>
  <div class="frame-band"></div>
  <div class="frame-inner"></div>
  <div class="corner-ornament top-left" role="img" aria-label="Gold scroll corner ornament"></div>
  <div class="corner-ornament top-right" role="img" aria-label="Gold scroll corner ornament"></div>
  <div class="corner-ornament bottom-left" role="img" aria-label="Gold scroll corner ornament"></div>
  <div class="corner-ornament bottom-right" role="img" aria-label="Gold scroll corner ornament"></div>

  <div class="paper">
    <svg class="watermark" role="img" aria-label="Security watermark: repeated institute name">
      <defs>
        <pattern id="watermark-pattern" width="300" height="110" patternUnits="userSpaceOnUse" patternTransform="rotate(-24)">
          <text x="10" y="40">Marlow Institute</text>
          <text x="160" y="95">Marlow Institute</text>
        </pattern>
      </defs>
      <rect width="100%" height="100%" fill="url(#watermark-pattern)"/>
    </svg>
  </div>

  <svg class="institution-title" viewBox="0 0 1030 220" aria-label="Marlow Institute">
    <defs>
      <path id="title-arc" d="M 10 205 Q 515 35 1020 205"/>
    </defs>
    <text class="title-shadow" transform="translate(5 5)"><textPath href="#title-arc" startOffset="50%" text-anchor="middle">Marlow Institute</textPath></text>
    <text><textPath href="#title-arc" startOffset="50%" text-anchor="middle">Marlow Institute</textPath></text>
  </svg>

  <p class="line recommendation">Upon the recommendation by</p>
  <p class="line faculty">Faculty of Business and Management</p>
  <p class="line student-name">Student Name</p>
  <p class="line completion">has satisfactorily completed the studies prescribed and earned the</p>
  <p class="line award">Advanced Diploma of Management</p>
  <p class="line rights">with all the rights, privileges and honors pertaining to that degree.</p>
  <p class="line presented">Presented this fifteenth day of May, two thousand and thirteen</p>

  <div class="signature-block president">
    <div class="signature-mark" role="img" aria-label="Handwritten signature of the president"></div>
    <p class="signatory-name">Clara Whitby</p>
    <p class="signatory-role">President of the college</p>
  </div>

  <div class="signature-block board">
    <div class="signature-mark" role="img" aria-label="Handwritten signature of the board representative"></div>
    <p class="signatory-name">Owen Castell</p>
    <p class="signatory-role">College board of education</p>
  </div>

  <div class="seal-panel">
    <div class="seal-square"></div>
    <p class="seal-name">Marlow Institute</p>
  </div>
</main>
</body>
</html>
```